Private School Marketing Postcard

We are a commercial printing and mailing company. We are planning on starting a postcard mailing campaign targeted at private schools in Connecticut and Westchester County, NY. We are promoting our printing and mailing services and we are not sure how our postcards should be designed or what our advertising concept will be. We are looking for someone to come up with a postcard concept and design for our mailing campaign. (We will mail at least 3 versions in sequential mailings)

Target Market(s)

Private Schools

Industry/Entity Type

School

Font styles to use
Serif

Requirements
Must have
• Our Logo
• Harborline Press and Mailing, Inc.
• 47 Alder Lane
• Norwalk, CT 06914
• www.harborlinepress.example
• 203.555.0187
• dave@harborlinepress.example
• Right half of side 2 must be blank for mailing panel

```html
<!DOCTYPE html>
<html lang="en">
<head>
<meta charset="utf-8">
<title>Harborline Press and Mailing – School Postcard</title>
<link rel="stylesheet" href="https://fonts.googleapis.com/css2?family=Jost:wght@400&family=Pathway+Gothic+One&display=swap">
<style>
  :root {
    --stage: #2b2b2b;
    --cream-light: #fffdf1;
    --cream: #fff6c4;
    --maroon: #9b1b1e;
    --ink: #1f1f1f;
    --teal: #2fb8cf;
    --teal-soft: #bfe9ee;
    --panel: #f2f2f2;
    --badge: #135a7c;
    --sky: #6f97d6;
    --building: #c9c9c9;
    --road: #4a4a4a;
  }
  * { margin: 0; padding: 0; box-sizing: border-box; }
  html, body { width: 960px; height: 1200px; overflow: hidden; }
  body { background: var(--stage); position: relative; font-family: "Jost", sans-serif; color: var(--ink); }

  .card {
    position: absolute; left: 91px; width: 775px; height: 501px;
    background: linear-gradient(100deg, var(--cream-light) 0%, var(--cream) 60%);
    overflow: hidden;
  }
  .card--front { top: 60px; }
  .card--back { top: 632px; }
  .card svg.shapes { position: absolute; inset: 0; }

  .brand { position: absolute; display: flex; flex-direction: column; align-items: center; }
  .brand__mark { width: 58px; height: 58px; border-radius: 50%; background: var(--maroon); }
  .brand__name {
    margin-top: 12px; font-size: 14px; letter-spacing: 2.5px; line-height: 1.5;
    color: var(--maroon); text-align: center; text-transform: uppercase;
  }
  .card--front .brand { left: 32px; top: 26px; }
  .card--back .brand { left: 40px; top: 26px; }

  .headline-band {
    position: absolute; left: 0; top: 170px; width: 360px; height: 98px;
    background: linear-gradient(90deg, var(--teal-soft) 0%, rgba(191,233,238,0) 100%);
    padding: 12px 0 0 34px;
    font-family: "Pathway Gothic One", sans-serif; font-size: 30px; line-height: 38px; color: var(--ink);
  }
  .pitch {
    position: absolute; left: 34px; top: 296px;
    font-family: "Pathway Gothic One", sans-serif; font-size: 28px; line-height: 36px; color: var(--maroon);
  }
  .web-line { position: absolute; left: 34px; top: 392px; font-size: 16px; display: flex; align-items: center; gap: 8px; }
  .phone-band {
    position: absolute; left: 0; top: 440px; width: 420px; height: 45px;
    background: linear-gradient(90deg, var(--teal) 0%, #6fd0df 70%, rgba(111,208,223,0) 100%);
    display: flex; align-items: center; gap: 12px; padding-left: 28px;
    font-family: "Pathway Gothic One", sans-serif; font-size: 32px; color: #fff;
  }

  .accreditation-badge { position: absolute; left: 243px; top: 37px; width: 118px; height: 44px; background: var(--badge); border-radius: 5px; }
  .contact-title { position: absolute; left: 43px; top: 180px; font-size: 28px; color: var(--maroon); font-weight: 400; }
  .contact-list { position: absolute; left: 40px; top: 226px; list-style: none; font-size: 21px; line-height: 27px; }
  .contact-list li { display: flex; align-items: flex-start; }
  .contact-list .icon { flex: none; width: 29px; display: flex; justify-content: center; padding-top: 5px; }
  .social { position: absolute; left: 48px; top: 383px; display: flex; gap: 15px; }
  .social span { width: 27px; height: 27px; border-radius: 50%; background: var(--ink); }
  .stamp-box { position: absolute; left: 642px; top: 34px; width: 99px; height: 105px; border: 1px solid #333; }
  .address-line { position: absolute; left: 490px; width: 250px; height: 1px; background: #333; }
  .footer-strip { position: absolute; left: 163px; top: 434px; width: 612px; height: 67px; background: #fff; }
</style>
</head>
<body>

<section class="card card--front" aria-label="Postcard front">
  <svg class="shapes" width="775" height="501" viewBox="0 0 775 501">
    <defs>
      <linearGradient id="photoTone" x1="0" y1="0" x2="0" y2="1">
        <stop offset="0" stop-color="var(--sky)"/>
        <stop offset="0.45" stop-color="#b6c6e0"/>
        <stop offset="0.6" stop-color="var(--building)"/>
        <stop offset="1" stop-color="var(--road)"/>
      </linearGradient>
    </defs>
    <path d="M456,0 C400,80 370,180 385,270 C398,350 432,420 402,501 L425,501 C452,420 418,350 405,270 C390,180 420,80 474,0 Z" fill="var(--maroon)"/>
    <path role="img" aria-label="Photo of a school building entrance with a mail delivery truck parked out front"
          d="M474,0 C420,80 390,180 405,270 C418,350 452,420 425,501 L775,501 L775,0 Z" fill="url(#photoTone)"/>
  </svg>

  <div class="brand">
    <span class="brand__mark"></span>
    <span class="brand__name">Harborline Press<br>and Mailing, Inc.</span>
  </div>

  <div class="headline-band">Commercial Printing with<br>Exceptional Service and Quality</div>
  <p class="pitch">Trust Harborline Press and Mailing, Inc.<br>With your next Project.</p>

  <p class="web-line">
    <svg width="18" height="18" viewBox="0 0 18 18" fill="none" stroke="var(--maroon)" stroke-width="1.4"><circle cx="9" cy="9" r="7.5"/><ellipse cx="9" cy="9" rx="3.2" ry="7.5"/><path d="M1.5 9h15M3 5h12M3 13h12"/></svg>
    www.harborlinepress.example
  </p>

  <div class="phone-band">
    <svg width="28" height="28" viewBox="0 0 28 28" fill="none" stroke="#fff" stroke-width="2"><circle cx="14" cy="14" r="12.5"/><path d="M9.5 7.5l2.5 3-1.5 2c1 2 2.5 3.5 4.5 4.5l2-1.5 3 2.5-1.5 2.5c-5 0-10.5-5.5-10.5-10.5z" fill="#fff" stroke="none"/></svg>
    203.555.0187
  </div>
</section>

<section class="card card--back" aria-label="Postcard back">
  <svg class="shapes" width="775" height="501" viewBox="0 0 775 501">
    <path d="M458,0 C400,60 362,140 380,220 C398,300 446,360 448,434 L466,434 C464,360 416,300 398,220 C380,140 418,60 476,0 Z" fill="var(--maroon)"/>
    <path d="M476,0 C418,60 380,140 398,220 C416,300 464,360 466,434 L775,434 L775,0 Z" fill="var(--panel)"/>
  </svg>

  <div class="brand">
    <span class="brand__mark"></span>
    <span class="brand__name">Harborline Press<br>and Mailing, Inc.</span>
  </div>
  <div class="accreditation-badge" role="img" aria-label="Accreditation badge"></div>

  <h2 class="contact-title">Contact Info</h2>
  <ul class="contact-list">
    <li><span class="icon"><svg width="16" height="18" viewBox="0 0 16 18" fill="none" stroke="var(--maroon)" stroke-width="1.6"><path d="M8 13C4 8.5 3 6.5 3 5a5 5 0 0110 0c0 1.5-1 3.5-5 8z"/><circle cx="8" cy="5" r="1.8"/><path d="M2 17h12"/></svg></span><span>47 Alder Lane<br>Norwalk, CT 06914</span></li>
    <li><span class="icon"><svg width="16" height="16" viewBox="0 0 18 18" fill="none" stroke="var(--maroon)" stroke-width="1.4"><circle cx="9" cy="9" r="7.5"/><ellipse cx="9" cy="9" rx="3.2" ry="7.5"/><path d="M1.5 9h15M3 5h12M3 13h12"/></svg></span><span>www.harborlinepress.example</span></li>
    <li><span class="icon"><svg width="16" height="16" viewBox="0 0 28 28" fill="none" stroke="var(--maroon)" stroke-width="2.4"><circle cx="14" cy="14" r="12.5"/><path d="M9.5 7.5l2.5 3-1.5 2c1 2 2.5 3.5 4.5 4.5l2-1.5 3 2.5-1.5 2.5c-5 0-10.5-5.5-10.5-10.5z" fill="var(--maroon)" stroke="none"/></svg></span><span>203.555.0187</span></li>
    <li><span class="icon"><svg width="18" height="14" viewBox="0 0 18 14" fill="none" stroke="var(--maroon)" stroke-width="1.4"><rect x="1" y="1" width="16" height="12"/><path d="M1 1l8 6 8-6M1 13l6-5M17 13l-6-5"/></svg></span><span>dave@harborlinepress.example</span></li>
  </ul>

  <div class="social" aria-label="Social links"><span></span><span></span><span></span><span></span><span></span><span></span></div>

  <div class="stamp-box"></div>
  <div class="address-line" style="top:275px"></div>
  <div class="address-line" style="top:311px"></div>
  <div class="address-line" style="top:347px"></div>
  <div class="footer-strip"></div>
</section>

</body>
</html>
```